Moss and Stone Distillery gin labels

Moss and Stone Distillery, Caithness, Scotland
Background information
The name Moss and Stone comes from the aurora borealis which we see all winter in the Caithness skies. I see the aurora from my back door and often watch it through the night. People often think that you can only see the aurora in Iceland or Norway but stunning examples of what we see are on vid stream (see following links)
https://www.vidstreamly.example/watch?v=kdLe-xTR4wq
https://www.vidstreamly.example/watch?v=mBrUTe-9pZa
Moss and Stone Distillery will be a family venture consisting of three families who are crofters in the same area.
We are looking for labels for our first gins to be produced. The first will be called Bramblemoor Gin or Bramblemoor Upland Gin and the second gin is called Shepherd’s Sorrow. We are looking for label imagery that can be used a across a range of different gins that we will produce. We want the labels to evoke a luxury, premium brand as this will be at the top end of the gin pricing range. Gold or copper lettering/colours will tie in with our copper stills. We need the design to stand out on the shelf amongst a sea of gins in predominantly clear bottles with a lot of white labels. We need something with shelf appeal and something that is distinct on the bar shelf so it stands out from the others.

Target Market(s)

premium high end market

Font styles to use
Decorative
Script

Colors

Designer to choose colors to be used in the design.

Requirements
Must have
• stand out on the shelf impact
• premium luxury look to the labels
Nice to have
• something that is makes the Scottish Highland Gin theme stand out

```html
<!DOCTYPE html>
<html lang="en">
<head>
<meta charset="utf-8">
<title>Bramblemoor Upland Gin – Label</title>
<link rel="stylesheet" href="https://fonts.googleapis.com/css2?family=Cinzel:wght@600;700&family=Oswald:wght@500&family=Libre+Baskerville:wght@700&display=swap">
<style>
  :root {
    --backdrop: #e2e2e2;
    --copper-light: #f4a12a;
    --copper-mid: #d9811a;
    --copper-dark: #9a4d0e;
    --cream: #f3efd6;
    --panel: #e9ebd2;
    --ink: #141210;
    --border-brown: #5a2d0a;
  }
  * { margin: 0; padding: 0; box-sizing: border-box; }
  html, body {
    width: 1200px; height: 1200px; overflow: hidden;
    background: var(--backdrop);
  }
  .label {
    position: absolute; left: 270px; top: 132px;
    width: 660px; height: 935px;
  }
  .label-shape { position: absolute; inset: 0; width: 660px; height: 935px; }
  .ornament {
    position: absolute;
    background: linear-gradient(180deg, #2a221a, #0e0c0a);
    opacity: .85;
  }
  .crown { left: 300px; top: 96px; width: 60px; height: 46px; border-radius: 6px 6px 2px 2px; }
  .flourish-top { left: 210px; top: 292px; width: 240px; height: 18px; border-radius: 9px; opacity: .7; }
  .flourish-mid { left: 270px; top: 486px; width: 120px; height: 16px; border-radius: 8px; opacity: .7; }
  .flourish-low { left: 270px; top: 648px; width: 120px; height: 14px; border-radius: 7px; opacity: .7; }
  .text { position: absolute; left: 0; width: 660px; text-align: center; color: var(--ink); }
  .brand {
    top: 140px; font-family: "Cinzel", serif; font-weight: 700;
    font-size: 52px; letter-spacing: 1px; line-height: 66px;
  }
  .product-name {
    top: 318px; font-family: "Oswald", sans-serif; font-weight: 500;
    font-size: 132px; line-height: 150px; letter-spacing: 2px;
    text-shadow: 3px 3px 0 rgba(0,0,0,.18);
  }
  .product-type {
    top: 512px; font-family: "Oswald", sans-serif; font-weight: 500;
    font-size: 104px; line-height: 128px; letter-spacing: 2px;
    text-shadow: 3px 3px 0 rgba(0,0,0,.18);
  }
  .distillery-mark {
    position: absolute; left: 478px; top: 522px; width: 116px; height: 116px;
    border: 3px solid var(--ink); border-radius: 50%;
    display: flex; align-items: center; justify-content: center; text-align: center;
    font-family: "Libre Baskerville", serif; font-weight: 700;
    font-size: 13px; line-height: 17px; color: var(--ink);
    background: var(--cream);
  }
  .style-line {
    top: 700px; font-family: "Libre Baskerville", serif; font-weight: 700;
    font-size: 30px; line-height: 42px; letter-spacing: 1px; color: #1e120a;
  }
  .spec-row {
    position: absolute; left: 90px; top: 770px; width: 480px;
    display: flex; justify-content: space-between;
    font-family: "Libre Baskerville", serif; font-weight: 700;
    font-size: 30px; line-height: 40px; color: #1e120a;
  }
  .volume {
    top: 852px; font-family: "Libre Baskerville", serif; font-weight: 700;
    font-size: 30px; line-height: 40px; color: #1e120a;
  }
</style>
</head>
<body>
  <div class="label">
    <svg class="label-shape" viewBox="0 0 660 935" aria-hidden="true">
      <defs>
        <linearGradient id="copper" x1="0" y1="0" x2="1" y2="0">
          <stop offset="0" stop-color="#b65e12"/>
          <stop offset=".3" stop-color="#e88c1e"/>
          <stop offset=".65" stop-color="#f6a62c"/>
          <stop offset="1" stop-color="#c46a14"/>
        </linearGradient>
        <linearGradient id="panel-grad" x1="0" y1="0" x2="0" y2="1">
          <stop offset="0" stop-color="#eef0d8"/>
          <stop offset="1" stop-color="#e4e6ca"/>
        </linearGradient>
      </defs>
      <path d="M0 100 C0 40 60 30 120 22 Q330 -8 540 22 C600 30 660 40 660 100 L660 835 C660 895 600 905 540 913 Q330 943 120 913 C60 905 0 895 0 835 Z" fill="#7a3c0c"/>
      <path transform="translate(5 5) scale(0.9848 0.9893)" d="M0 100 C0 40 60 30 120 22 Q330 -8 540 22 C600 30 660 40 660 100 L660 835 C660 895 600 905 540 913 Q330 943 120 913 C60 905 0 895 0 835 Z" fill="var(--cream)"/>
      <path transform="translate(12 12) scale(0.9636 0.9743)" d="M0 100 C0 40 60 30 120 22 Q330 -8 540 22 C600 30 660 40 660 100 L660 835 C660 895 600 905 540 913 Q330 943 120 913 C60 905 0 895 0 835 Z" fill="url(#copper)"/>
      <path transform="translate(24 24) scale(0.9273 0.9487)" d="M0 100 C0 40 60 30 120 22 Q330 -8 540 22 C600 30 660 40 660 100 L660 835 C660 895 600 905 540 913 Q330 943 120 913 C60 905 0 895 0 835 Z" fill="none" stroke="#3a1a04" stroke-width="2.5"/>
      <rect x="26" y="232" width="608" height="456" fill="var(--cream)"/>
      <rect x="26" y="232" width="608" height="456" fill="none" stroke="var(--cream)" stroke-width="6" stroke-dasharray="6 6"/>
      <rect x="36" y="244" width="588" height="432" fill="url(#panel-grad)" stroke="#3a2a1a" stroke-width="2.5"/>
      <line x1="110" y1="472" x2="550" y2="472" stroke="var(--ink)" stroke-width="4"/>
      <circle cx="110" cy="472" r="5" fill="var(--ink)"/>
      <circle cx="550" cy="472" r="5" fill="var(--ink)"/>
      <rect x="228" y="510" width="204" height="134" fill="none" stroke="var(--ink)" stroke-width="3"/>
      <rect x="236" y="518" width="188" height="118" fill="none" stroke="var(--ink)" stroke-width="2"/>
      <line x1="90" y1="756" x2="570" y2="756" stroke="#2a1608" stroke-width="2" stroke-dasharray="7 5"/>
    </svg>

    <div class="ornament crown" role="img" aria-label="Small crown ornament above the brand name"></div>
    <div class="text brand">BRAMBLEMOOR</div>
    <div class="ornament flourish-top" role="img" aria-label="Scrollwork flourish divider"></div>
    <div class="text product-name">UPLAND</div>
    <div class="ornament flourish-mid" role="img" aria-label="Scrollwork flourish divider"></div>
    <div class="text product-type">GIN</div>
    <div class="ornament flourish-low" role="img" aria-label="Scrollwork flourish divider"></div>
    <div class="distillery-mark">Moss and<br>Stone<br>Distillery</div>

    <div class="text style-line">NAVY STRENGTH GIN</div>
    <div class="spec-row"><span>57% Alc./Vol.</span><span>70cl</span></div>
    <div class="text volume">750 ML.</div>
  </div>
</body>
</html>
```